We are seeking two label designs for our premium pecan snack brand, TORVELLO. TORVELLO is known for its innovative pecan snacks, specifically a healthy and exotic blend of pecans, expertly salted, and infused with unique chili flavors. Our snacks are packaged in stand-up pouch bags, and we are looking for label designs product sizes - 5 oz. ( Size: 14 x 20 cm / 5.5 x 7.8 inches / Max Capacity: 16.2 oz)

Background Information:
TORVELLO is a brand committed to offering a delightful snacking experience that combines the natural richness of pecans with the bold and exotic kick of carefully selected chilies. Our snacks cater to health-conscious consumers who appreciate the fusion of premium quality, unique flavors, and nutritional goodness.

Target Market(s)

Event Attendees (Entertainment Industry), Health-Conscious Consumers

Industry/Entity Type

Entertainment (sports events, arenas, stadiums, etc)

Font styles to use
Other font styles liked:
• Brother1816 Printed

Colors

Designer to choose colors to be used in the design.

Requirements
Must have
• Nutrition Fact (attached) , TRANSPARENT PART LIKE A WINDOW TO DISPLAY THE PRODUCT

```html
<!DOCTYPE html>
<html lang="en">
<head>
<meta charset="utf-8">
<title>TORVELLO – Spicey Pecan Nuts Pouch Label</title>
<link rel="stylesheet" href="https://fonts.googleapis.com/css2?family=Josefin+Sans:wght@600;700&family=Montserrat:wght@700&display=swap">
<style>
  :root {
    --backdrop: #f47a4d;
    --pouch: #050505;
    --disc: #171717;
    --disc-rim: #2b2b2b;
    --brand-white: #ffffff;
    --accent: #f0703e;
    --weight-brown: #b8653d;
    --nut-light: #c98a5a;
    --nut-dark: #7a4325;
  }
  * { margin: 0; padding: 0; box-sizing: border-box; }
  html, body {
    width: 1197px;
    height: 1200px;
    overflow: hidden;
    background: var(--backdrop);
  }
  .canvas {
    position: relative;
    width: 1197px;
    height: 1200px;
    background: var(--backdrop);
  }
  .pouch-label {
    position: absolute;
    left: 346px;
    top: 150px;
    width: 505px;
    height: 800px;
    background: var(--pouch);
    border-radius: 14px;
  }
  .brand-name {
    position: absolute;
    top: 165px;
    left: 0;
    width: 100%;
    text-align: center;
    font-family: "Josefin Sans", sans-serif;
    font-weight: 700;
    font-size: 68px;
    letter-spacing: 2px;
    line-height: 1;
    color: var(--brand-white);
  }
  .tagline {
    position: absolute;
    top: 292px;
    left: 50%;
    transform: translateX(-50%);
    padding: 6px 0 5px;
    border-top: 1.5px solid var(--accent);
    border-bottom: 1.5px solid var(--accent);
    font-family: "Josefin Sans", sans-serif;
    font-weight: 600;
    font-size: 17px;
    letter-spacing: 3.6px;
    line-height: 1;
    color: var(--accent);
    white-space: nowrap;
  }
  .window-art {
    position: absolute;
    left: 0;
    top: 0;
    width: 505px;
    height: 800px;
  }
  .net-weight {
    position: absolute;
    top: 750px;
    left: 0;
    width: 100%;
    text-align: center;
    font-family: "Montserrat", sans-serif;
    font-weight: 700;
    font-size: 18px;
    color: var(--weight-brown);
  }
</style>
</head>
<body>
  <main class="canvas">
    <section class="pouch-label">
      <svg class="window-art" viewBox="0 0 505 800" xmlns="http://www.w3.org/2000/svg">
        <defs>
          <linearGradient id="nutTone" x1="0" y1="0" x2="1" y2="1">
            <stop offset="0" stop-color="var(--nut-light)"/>
            <stop offset="1" stop-color="var(--nut-dark)"/>
          </linearGradient>
        </defs>
        <circle class="feature-disc" cx="252" cy="561" r="170" fill="var(--disc)" stroke="var(--disc-rim)" stroke-width="4"/>
        <ellipse class="pecan-illustration" cx="270" cy="482" rx="78" ry="52" fill="var(--accent)" opacity="0.25"
                 role="img" aria-label="Line drawing of pecan nuts with leaves"/>
        <path class="product-window"
              d="M108,359 C40,430 50,600 160,670 C270,730 420,650 459,502 C400,565 240,580 175,505 C135,460 115,410 108,359 Z"
              fill="url(#nutTone)" role="img" aria-label="Transparent window showing the pecan nuts inside"/>
      </svg>
      <h1 class="brand-name">TORVELLO</h1>
      <p class="tagline">SPICEY PECAN NUTS</p>
      <p class="net-weight">155 g NETT</p>
    </section>
  </main>
</body>
</html>
```